Award winning Indie press looking for a world class book cover for global relaunch

We need to update a book cover for one of our titles which is being relaunched. The title will exist in both physical and e-formats.
The book is genre specific and era specific. World war 2, Greece. Beneath the Pale Hills is a compelling work of literary fiction, a war novel that explores the challenges of peace. A gripping historical adventure, it paints a portrait of courage and love in the fatal shadow of global conflict that has spilled into the twenty-first century.
Usage of the provided images is of course optional but it is a book about the German occupation of Greece. Images are public domain.
The cover needs to convey a sense of drama, typical for war novels.
Necessary information.
Size: A5
Title: Beneath the Pale Hills
Author: Martin Ashcombe
Blurb: An excellent book - Fairbridge Ledger UK
Publisher: logo- provided
Spine: Spine: 0.785 inches or 19.93 mm
Back cover text: Occupied Greece 1943. Beneath the Pale Hills is a compelling work of literary fiction, a war novel that also explores the challenges of peace. A gripping historical adventure, it paints a portrait of courage and love in the fatal shadow of global conflict that has spilled tragically into the twenty-first century.
Citizens of Nazi-occupied Greece face daily decisions that affect their freedom and their survival. When music teacher Stavros intervenes in a dispute between a Greek woman and a German soldier, he and jazz singer Irini are plunged into the brutal world of armed resistance.
Neil Hartwell, a British agent, lands in Northern Greece, where he joins Stavros’ and Irini’s network. Never fully understanding his Greek collaborators, he forms a deep bond with them.
In Scotland after World War Two, Neil is alienated from everyday life until he meets Judith, an up and coming intelligence officer. Surrounded by opportunity and courted by influential mentors, Neil and Judith learn that integrity has to be fought for in peacetime Britain just as in wartime Europe.
When Neil undertakes a final mission to Greece, now in the full throes of civil war, the weight of ideology and history descends with sudden force on the small town where former friends and enemies confront one another in a terrifying climax.
Please allow approximately 2cm height X 3 cm length for the bar code.
Reason: Decided to allow more time as this is proving a bit more tricky than expected.

```html
<!DOCTYPE html>
<html lang="en">
<head>
<meta charset="utf-8">
<title>Beneath the Pale Hills – Cover Wrap</title>
<link rel="stylesheet" href="https://fonts.googleapis.com/css2?family=Cinzel:wght@400;500&family=Tinos&display=swap">
<style>
  :root {
    --paper: #d8d5cf;
    --paper-light: #e6e4df;
    --paper-dark: #b3afa7;
    --ink: #1a1816;
    --ink-warm: #5a2c18;
    --signal-red: #d2231c;
    --photo-black: #1e1c1a;
    --photo-dark: #3a3733;
    --photo-mid: #77726a;
    --photo-light: #c4c0b8;
    --photo-pale: #e4e1db;
    --sun: #fbf2df;
    --flag-red: #c8432c;
  }
  * { box-sizing: border-box; margin: 0; padding: 0; }
  html, body { width: 1200px; height: 892px; overflow: hidden; background: var(--paper); }
  .cover-wrap {
    position: relative; width: 1200px; height: 892px; overflow: hidden;
    background: radial-gradient(ellipse at 30% 20%, var(--paper-light), var(--paper) 55%, var(--paper-dark));
    font-family: "Tinos", "Times New Roman", serif; color: var(--ink);
  }
  .title { font-family: "Cinzel", "Times New Roman", serif; font-weight: 400; line-height: 1; }
  .title .big { display: block; }
  .title .small { display: block; letter-spacing: 2px; }

  /* Back cover */
  .back { position: absolute; left: 0; top: 0; width: 555px; height: 892px; }
  .back-photo {
    position: absolute; left: 0; top: 440px; width: 555px; height: 452px;
    background:
      linear-gradient(to bottom, var(--paper) 0%, rgba(216,213,207,0) 30%),
      linear-gradient(to right, var(--photo-black) 0%, var(--photo-dark) 12%, var(--photo-mid) 40%, var(--photo-light) 75%, var(--paper) 100%);
  }
  .back .title { position: absolute; left: 52px; top: 34px; }
  .back .title .big { font-size: 54px; letter-spacing: 1px; }
  .back .title .small { font-size: 24px; margin: 2px 0 0 72px; }
  .back .title .cap { font-size: 82px; }
  .blurb {
    position: absolute; left: 52px; top: 197px; width: 466px;
    font-size: 15px; line-height: 21.5px; text-align: justify; text-align-last: center;
  }
  .blurb p:first-child { text-indent: 8px; }

  /* Spine */
  .spine {
    position: absolute; left: 555px; top: 0; width: 88px; height: 892px;
    background: linear-gradient(to right, var(--paper-dark), var(--paper) 25%, var(--paper) 75%, var(--paper-dark));
  }
  .spine-title, .spine-author {
    position: absolute; left: 50%; transform: translateX(-50%);
    writing-mode: vertical-rl; font-family: "Cinzel", serif; white-space: nowrap;
  }
  .spine-title { top: 56px; font-size: 30px; }
  .spine-title .small { font-size: 17px; }
  .spine-author { top: 478px; font-size: 32px; }

  /* Publisher name */
  .imprint {
    position: absolute; display: flex; align-items: center; gap: 6px;
    font-family: "Tinos", serif; font-size: 16px; letter-spacing: 1px; color: var(--signal-red);
  }
  .imprint .mark { width: 11px; height: 11px; background: var(--signal-red); }
  .back .imprint { left: 8px; top: 856px; }
  .spine .imprint { left: 0; width: 88px; justify-content: center; top: 857px; font-size: 14px; }

  /* Front cover */
  .front { position: absolute; left: 643px; top: 0; width: 557px; height: 892px; }
  .front-photo {
    position: absolute; left: 0; top: 200px; width: 557px; height: 692px;
    background:
      linear-gradient(to bottom, var(--paper) 0%, rgba(216,213,207,0) 14%),
      radial-gradient(circle at 86% 20%, var(--sun) 0%, rgba(251,242,223,.7) 8%, rgba(251,242,223,0) 26%),
      radial-gradient(ellipse 130px 200px at 30% 36%, var(--flag-red) 0%, rgba(200,67,44,.75) 55%, rgba(200,67,44,0) 100%),
      linear-gradient(to bottom,
        var(--photo-pale) 0%, var(--photo-light) 22%, var(--photo-mid) 36%,
        var(--photo-dark) 48%, var(--photo-black) 66%, var(--photo-dark) 76%,
        var(--photo-light) 86%, var(--photo-pale) 100%);
  }
  .front .title { position: absolute; left: 0; width: 557px; top: 36px; text-align: center; }
  .front .title .big { font-size: 64px; letter-spacing: 2px; }
  .front .title .small { font-size: 28px; margin: 2px 0 0 40px; }
  .front .title .hills { font-size: 66px; color: var(--ink-warm); }
  .front .title .cap { font-size: 100px; color: var(--ink); }
  .review { position: absolute; left: 0; width: 557px; top: 362px; text-align: center; color: var(--ink); }
  .review q { font-size: 24px; quotes: "\201C" "\201D"; }
  .review cite { display: block; font-style: normal; font-size: 15px; margin-top: 2px; }
  .front-author {
    position: absolute; left: 0; width: 557px; top: 796px; text-align: center;
    font-family: "Cinzel", serif; font-size: 46px; color: var(--ink);
  }
  .front .imprint { left: 270px; top: 856px; }
</style>
</head>
<body>
<main class="cover-wrap">
  <section class="back">
    <div class="back-photo" role="img" aria-label="Faded wartime street photograph with a tank and soldiers"></div>
    <h2 class="title"><span class="big">BENEATH</span><span class="small">THE PALE</span><span class="big"><span class="cap">H</span>ILLS</span></h2>
    <div class="blurb">
      <p>Occupied Greece 1943. Beneath the Pale Hills is a compelling work of literary fiction, a war novel that also explores the challenges of peace. A gripping historical adventure, it paints a portrait of courage and love in the fatal shadow of global conflict that has spilled tragically into the twenty-first century.</p>
      <p>Citizens of Nazi-occupied Greece face daily decisions that affect their freedom and their survival. When music teacher Stavros intervenes in a dispute between a Greek woman and a German soldier, he and jazz singer Irini are plunged into the brutal world of armed resistance.</p>
      <p>Neil Hartwell, a British agent, lands in Northern Greece, where he joins Stavros’ and Irini’s network. Never fully understanding his Greek collaborators, he forms a deep bond with them.</p>
      <p>In Scotland after World War Two, Neil is alienated from everyday life until he meets Judith, an up and coming intelligence officer. Surrounded by opportunity and courted by influential mentors, Neil and Judith learn that integrity has to be fought for in peacetime Britain just as in wartime Europe. When Neil undertakes a final mission to Greece, now in the full throes of civil war, the weight of ideology and history descends with sudden force on the small town where former friends and enemies confront one another in a terrifying climax.</p>
    </div>
    <div class="imprint"><span class="mark"></span>KESTREL</div>
  </section>

  <section class="spine">
    <div class="spine-title">BENEATH <span class="small">THE PALE</span> HILLS</div>
    <div class="spine-author">MARTIN ASHCOMBE</div>
    <div class="imprint">KESTREL</div>
  </section>

  <section class="front">
    <div class="front-photo" role="img" aria-label="Black and white photograph of soldiers gathered around a raised red flag before an ancient temple ruin, sun glaring behind"></div>
    <h1 class="title"><span class="big">BENEATH</span><span class="small">THE PALE</span><span class="big hills"><span class="cap">H</span>ILLS</span></h1>
    <div class="review"><q>An excellent book</q><cite>- Fairbridge Ledger UK -</cite></div>
    <div class="front-author">MARTIN ASHCOMBE</div>
    <div class="imprint"><span class="mark"></span>KESTREL</div>
  </section>
</main>
</body>
</html>
```